Harbourline capital partners pty ltd

Hi guys I recently opened a brokerage company. I need a flyer to capture the attention of customers.
I would like something professional and cool at the same time.
My website is harbourcp.com.au
I also attached the current flyer. as you can see it lacks of originality and it isn't cool!!!!
Thank you

Target Market(s)

People between the age of 18-50

Industry/Entity Type

Financial Service

Requirements
Must have
• Mast have features and contents that reflects the website
• harbourcp.com.au
Nice to have
• Open to anything
Should not have
• Not to sure

```html
<!DOCTYPE html>
<html lang="en">
<head>
<meta charset="utf-8">
<title>Harbourline Capital Partners – Flyer</title>
<link href="https://fonts.googleapis.com/css2?family=Exo+2:wght@300;400;500&display=swap" rel="stylesheet">
<style>
:root{
  --stage:#8fa6a6;
  --paper:#f4f4f2;
  --ink:#1d1d1d;
  --ink-soft:#3a3a3a;
  --blue:#1f9ad6;
  --orange:#e8891c;
  --white:#ffffff;
  --gold:#c9a227;
  --green:#3f9a3a;
}
*{box-sizing:border-box;margin:0;padding:0}
html,body{width:1200px;height:960px;overflow:hidden}
body{background:var(--stage);font-family:"Exo 2",sans-serif;color:var(--ink);position:relative}
.flyer{position:absolute;left:270px;top:15px;width:660px;height:930px;background:var(--paper);overflow:hidden;box-shadow:0 6px 24px rgba(0,0,0,.18)}
.flyer > *{position:absolute}
.brand{top:34px;left:0;width:100%;text-align:center;color:var(--blue);font-weight:400;line-height:1}
.brand-name{font-size:31px;letter-spacing:1px}
.brand-sub{font-size:13px;letter-spacing:6px;margin-top:8px}
.intro{top:136px;left:25px;width:612px;font-size:16px;line-height:21px;font-weight:500;color:var(--ink)}
.heading{font-size:23px;font-weight:400;left:25px}
.heading.orange{color:var(--orange)}
.heading.blue{color:var(--blue)}
.specialise{top:255px}
.categories{top:288px;left:25px;font-size:19px;font-weight:500;color:var(--blue)}
.categories .orange{color:var(--orange)}
.financiers{top:326px}
.financiers-note{top:361px;left:25px;width:590px;font-size:16px;line-height:25px;font-weight:300;color:var(--ink-soft)}
.list{list-style:none;left:25px;font-size:15.5px;font-weight:500}
.list li{height:31px;line-height:31px;white-space:nowrap}
.dot{display:inline-block;width:5px;height:5px;border-radius:50%;margin:0 8px 3px 2px;vertical-align:middle}
.dot.b{background:var(--blue)} .dot.o{background:var(--orange)} .dot.k{background:var(--ink)}
.lenders{top:418px}
.why{top:517px}
.reasons{top:552px}
.reasons li.two{height:49px;line-height:24px;padding-top:4px}
.reasons .indent{padding-left:15px;display:block}
.artwork{left:120px;top:440px;width:540px;height:450px;clip-path:polygon(0% 100%,30% 70%,55% 50%,75% 30%,96% 0%,100% 0%,100% 100%);background:linear-gradient(160deg,#5fae4f 0%,var(--gold) 45%,#a5801c 100%);opacity:.9}
.bands{left:0;top:0;width:660px;height:930px}
.footer-name{left:30px;top:865px;font-size:30px;font-weight:400;color:var(--white);letter-spacing:1px}
.contact{right:22px;top:832px;text-align:right;list-style:none;color:var(--white);font-size:16.5px;font-weight:300}
.contact li{height:22px;line-height:22px}
.contact svg{width:11px;height:11px;margin-left:5px;vertical-align:-1px}
</style>
</head>
<body>
<main class="flyer">
  <div class="brand">
    <div class="brand-name">HARBOURLINE CAPITAL</div>
    <div class="brand-sub">PARTNERS PTY LTD</div>
  </div>

  <p class="intro">Harbourline capital partners is a bespoke brokerage firm established by a team of professionals who bring with them over 50 year’s combined experience in consulting, finance, negotiation, and executive roles within the finance and automotive industry. We strive for excellence, delivering the right solution for our clients in a timely and professional manner.</p>

  <h2 class="heading orange specialise">We specialise in financing</h2>
  <p class="categories">Cars | <span class="orange">Boats</span> | Caravans | <span class="orange">Jet skis</span> | Trucks | <span class="orange">Earth moving Equipment</span></p>

  <h2 class="heading blue financiers">Our Financiers include</h2>
  <p class="financiers-note">We have privileged and specialized access to a wide range of lenders enabling us to tailor solutions which cater to your individual needs. We work with:</p>

  <div class="artwork" role="img" aria-label="Stacks of gold coins rising in height with a green arrow bouncing upward across them"></div>

  <ul class="list lenders">
    <li><span class="dot b"></span>Bayview Finance <span class="dot o"></span>Kestrel Leasing <span class="dot b"></span>Autovale Finance</li>
    <li><span class="dot o"></span>Meridian Finance <span class="dot b"></span>Saltbush Asset finance <span class="dot o"></span>Torrent Motor Finance</li>
    <li><span class="dot k"></span>Union and Mutual Finance <span class="dot k"></span>Ridgeway Finance <span class="dot k"></span>QRB Finance</li>
  </ul>

  <h2 class="heading orange why">Why use us</h2>
  <ul class="list reasons">
    <li><span class="dot o"></span>Low rates <span class="dot b"></span>Access Australia’s most trusted lenders</li>
    <li><span class="dot o"></span>Quick &amp; easy, same day approvals</li>
    <li><span class="dot b"></span>Professional advice</li>
    <li class="two"><span class="dot o"></span>New, Used, private or<span class="indent">dealer sale - the choice is yours</span></li>
    <li><span class="dot b"></span>100% Finance available</li>
  </ul>

  <svg class="bands" viewBox="0 0 660 930" aria-hidden="true">
    <polygon points="0,765 0,930 232,930" fill="var(--orange)"/>
    <polygon points="210,930 660,930 660,772" fill="var(--blue)"/>
  </svg>

  <div class="footer-name">Harbourline</div>

  <ul class="contact">
    <li>+61 400 382 715<svg viewBox="0 0 12 12"><circle cx="6" cy="6" r="5" fill="none" stroke="currentColor"/><path d="M4 3.5l1 1.5-.7.7a4 4 0 0 0 2 2l.7-.7 1.5 1-.6 1A4.5 4.5 0 0 1 3 4.2z" fill="currentColor"/></svg></li>
    <li>www.harbourcp.com.au<svg viewBox="0 0 12 12"><circle cx="6" cy="6" r="5" fill="none" stroke="currentColor"/><path d="M1 6h10M6 1c2 2.5 2 7.5 0 10M6 1c-2 2.5-2 7.5 0 10" fill="none" stroke="currentColor" stroke-width=".8"/></svg></li>
    <li>admin@harbourcp.com.au<svg viewBox="0 0 12 12"><circle cx="6" cy="6" r="5" fill="none" stroke="currentColor"/><rect x="3.3" y="4" width="5.4" height="4" fill="none" stroke="currentColor" stroke-width=".8"/><path d="M3.3 4L6 6.2 8.7 4" fill="none" stroke="currentColor" stroke-width=".8"/></svg></li>
    <li>12 Wharf Street, Fyshwick ACT 2609<svg viewBox="0 0 12 12"><circle cx="6" cy="6" r="5" fill="none" stroke="currentColor"/><path d="M6 9.5S3.8 6.8 3.8 5.2a2.2 2.2 0 0 1 4.4 0C8.2 6.8 6 9.5 6 9.5z" fill="currentColor"/></svg></li>
  </ul>
</main>
</body>
</html>
```